Letterhead Design Project

I need letterhead designed for my law firm. It would also be used for web based stuff as well.

Industry/Entity Type

Law Firm

```html
<!DOCTYPE html>
<html lang="en">
<head>
<meta charset="utf-8">
<title>Harlow &amp; Vance Letterhead</title>
<link rel="stylesheet" href="https://fonts.googleapis.com/css2?family=Cinzel:wght@400&family=Questrial&display=swap">
<style>
  :root {
    --paper: #fbfbf6;
    --name-grey: #c4c4be;
    --contact-ink: #4a4a48;
    --mark-grey: #d6d6d0;
  }
  html, body {
    margin: 0;
    padding: 0;
    overflow: hidden;
    background: var(--paper);
  }
  .letterhead {
    position: relative;
    width: 848px;
    height: 1200px;
    background: var(--paper);
    overflow: hidden;
  }
  .letterhead__header {
    position: absolute;
    top: 40px;
    left: 0;
    width: 100%;
    text-align: center;
  }
  .firm-name {
    margin: 0;
    font-family: "Cinzel", serif;
    font-weight: 400;
    font-size: 34px;
    letter-spacing: 3px;
    line-height: 1;
    color: var(--name-grey);
  }
  .firm-contact {
    margin: 10px 0 0;
    font-family: "Questrial", sans-serif;
    font-size: 13px;
    line-height: 18px;
    color: var(--contact-ink);
  }
  .firm-signoff {
    position: absolute;
    right: 44px;
    bottom: 62px;
    width: 184px;
    margin: 0;
    text-align: right;
    font-family: "Cinzel", serif;
    font-weight: 400;
    font-size: 19px;
    letter-spacing: 1px;
    line-height: 1;
    color: var(--mark-grey);
  }
</style>
</head>
<body>
  <main class="letterhead">
    <header class="letterhead__header">
      <h1 class="firm-name">Harlow &amp; Vance</h1>
      <p class="firm-contact">
        238 Linden Avenue NW, Washington, DC 20005<br>
        (202) 555-0184
      </p>
    </header>
    <p class="firm-signoff" aria-hidden="true">Harlow &amp; Vance</p>
  </main>
</body>
</html>
```